Corporate website design needed

We need a Contemporary Industrial/Tech/Logistics Website design to match our logistic client's business. Our client consults and build logistics solutions that they manage but they are not a typical 3PL (3rd party logistics company) which is primarily engaged in moving boxes.
PSD file only for now, home and default templates.
COMPANY CHARACTER
DESIGN LOOK AND FEEL
• The design should also be modern and visually well organized — employing a combination of visual devices and info graphics. Keep it light and not too heavy but strong/ professional. And unique.
• The design should go beyond the typical industrial pick and pack 3PL representing [Logistics Company] as a High Tech/IT logistics company.
Some examples although these are not right for this client because they have much more content and present themselves more as a 3pl.
http://www.vh-gateway.example/ (More right then wrong - Like this but simplified)
http://www.dorantfreight.example (Ugly)
http://www.plmarwick.example (More right then wrong but different focus)
http://www.tellwinhaul.example/ Too 3PL trucking… We want a bit ore high level approach
The difference, the design should be a fusion in core concepts that culminate in a design which implies the following attributes. Tech (Big data / analytics / software), Consultancy (Solutions, SME, Leader), 3PL Industry vertical solutions.
NOTE: The visualization of “tech” is not “1” and “0”, but more “software and analytics” Perhaps more like www.metrivane.example.
• They need to be seen as a solutions provider in Logistics and as in Subject matter experts
TONE
The tone needs to exude professionalism, expertise, though leadership along with technical and executional excellence.
Experienced
Knowledgeable
Confident
Determined
Straightforward
WEBSITE OBJECTIVES
• Focus C-Suite executives and logistics managers’ attention on [Logistics Company]s commanding knowledge and expertise, and unique approach to supply chain solutions producing more RFP wins
• Create an easy to scan design which decreases the reliance on text through featured text, summaries, and smaller “chunked” size bits of information.
• Convey [Logistics Company] as high-tech 3PL solutions developer and services provider with a ‘high-touch’ consultative approach.
• Showcase [Logistics Company]’s value propositions. (See Slider Content)
• Showcase [Logistics Company]’s expertise in logistical analytics.
• Gain recognition as an industry leader in evolutionary new space (supply chain 2.0)
WEBSITE STRATEGY
• Reduce reliance on text (at least within initial entry points for each section)
• Typography: Watch text line lengths and readability, bolder fonts. NO SERIFS
• Generally, create a click-through format so that users who want more details can find it, and those who don’t can get a snapshot without clicking through.
• Increase visual content through info graphics and some dynamic content, photography
• Better utilize the space on each page (e.g., add visual interest, photography and iconography where appropriate to break up copy blocks and maintain readable line lengths).
COLOR SCHEME
• Create a more engaging color scheme (the logo will remain the same under all circumstances).
• Red / grayscale may work…. Not too dark or heavy. Not too much red. Ex. quorvik.example
• Also try blues and greys. They seem to like that. Open to suggestions but don’t get to crazy. Red is in their logo but too much may be a problem.
PHOTOGRAPHY
Yes. And I will upload some.
If you pick photography please be sure to note Which stock house used and the image number!
CONTENT
The content will be presented in a more hierarchical format — with lead-ins, paragraph and section headers and navigational cues to expand lengthier content allowing the visitor to more easily scan the website. No case studies, No Social media, News while on the home page should not be over emphasized. They don't post a lot so it gets dated quickly ...
I will be uploading a wire frame and other elements.
NOTE: I uploaded my EXAMPLE mock up which is close but not close enough.
I am not a great designer. So I am looking for an alternative that exceed my design ability! These examples show the basic layout but I really want some varied alternatives.
The colors are inconsistent and type not quite right. The grey bar at top is not right and should probably go away.
Please pull the basic elements in the example together into a great design.
If you have questions please contact me.
i will upload some photography tomorrow that may be of use.
Thanks!
Hi All,
We are still evaluating the submitted designs. Sorry for the delay.
This website is primarily a validation website. Few new customers will search and find them as such...
The site should be Focused on C-Suite executives and logistics managers’ attention on [Logistics Company]s commanding knowledge and expertise, and unique approach to supply chain solutions producing more RFP wins
Business
- Slide show, Clearly explain who they are and what they do.
Create an easy to scan design which decreases the reliance on text through featured text, summaries, and smaller “chunked” size bits of information.
Convey [Logistics Company] as high-tech 3PL solutions developer and services
provider with a ‘high-touch’ consultative approach.
- No Ads space
No Social media
Not too cluttered. Keep it clean.

```html
<!DOCTYPE html>
<html lang="en">
<head>
<meta charset="utf-8">
<title>Northvale Logistics</title>
<link href="https://fonts.googleapis.com/css2?family=Arimo:wght@400;700&family=Open+Sans:wght@400;600&family=Ubuntu:wght@500;700&family=Yanone+Kaffeesatz:wght@400&display=swap" rel="stylesheet">
<style>
:root{
  --red:#c4132f;
  --bar-grey:#9c9c9c;
  --panel-grey:#ebebeb;
  --head-grey:#6e6e6e;
  --tab-grey:#d9d9d9;
  --navy:#1b2847;
  --ink:#333;
  --body:#444;
  --footer:#1f1f1f;
  --footer-base:#141414;
  --white:#fff;
}
*{margin:0;padding:0;box-sizing:border-box}
html,body{width:734px;height:1200px;overflow:hidden;background:var(--white)}
body{font-family:"Arimo",Arial,sans-serif;color:var(--body)}
.canvas{position:relative;width:734px;height:1200px;overflow:hidden;background:var(--white)}
.abs{position:absolute}

.utility-bar{left:0;top:0;width:734px;height:26px;background:var(--bar-grey)}
.utility-links{right:80px;top:7px;font:600 9.5px "Open Sans",sans-serif;color:var(--white);display:flex;gap:11px;align-items:center}
.utility-links .call{color:var(--red)}
.utility-links .call span{color:var(--white)}
.search-icon{right:62px;top:7px;position:absolute}

.brand{display:flex;align-items:center;gap:8px}
.brand-dot{width:30px;height:30px;border-radius:50%;background:var(--red)}
.brand-name{font:600 12px "Open Sans",sans-serif;letter-spacing:3px;color:var(--ink);line-height:1.3}
.site-brand{left:70px;top:56px}

.main-nav{top:63px;left:380px;display:flex;align-items:center;font:400 10.5px "Open Sans",sans-serif;color:#222}
.main-nav a{color:inherit;text-decoration:none}
.nav-active{background:var(--red);color:var(--white)!important;width:74px;height:25px;display:flex;align-items:center;justify-content:center}
.nav-processes{margin-left:37px}
.nav-industries{margin-left:42px}

.content-panel{left:70px;top:346px;width:594px;height:658px;background:var(--panel-grey)}
.hero{left:72px;top:122px;width:590px;height:224px;background:var(--red);box-shadow:-14px 6px 22px rgba(0,0,0,.35),14px 6px 22px rgba(0,0,0,.35)}
.hero-art{left:0;top:0;width:300px;height:224px;background:linear-gradient(120deg,#dcdde2 0%,#c9ccd6 35%,#2a3558 55%,#d8c29a 80%,#c4132f 100%)}
.hero-title{left:323px;top:106px;font:700 20.5px "Ubuntu",sans-serif;color:var(--white);letter-spacing:.3px;white-space:nowrap}
.hero-sub{left:382px;top:132px;width:208px;height:23px;background:var(--white);font:500 14.5px "Ubuntu",sans-serif;color:#111;padding:3px 0 0 7px}
.hero-shadow{left:72px;top:346px;width:590px;height:26px;background:linear-gradient(#cfcfcf,var(--panel-grey))}
.slider-dots{left:337px;top:393px;display:flex;gap:4px}
.slider-dots span{width:10px;height:10px;border-radius:50%;border:1px solid #bbb;background:#f5f5f5}
.slider-dots span.on{background:#777;box-shadow:inset 0 0 0 2px #f5f5f5}

.welcome-title{left:79px;top:439px;font:400 21px "Yanone Kaffeesatz",sans-serif;color:var(--ink)}
.welcome-copy{left:80px;top:469px;width:360px;font-size:8.6px;line-height:11px;color:var(--body)}
.welcome-copy p{margin-bottom:11px}
.welcome-copy p.tight{margin-bottom:0}
.read-more{left:82px;top:671px;font:600 10px "Open Sans",sans-serif;color:var(--red)}

.side-box{background:#f4f4f4;border:1px solid #ddd}
.side-head{height:18px;background:var(--head-grey);color:var(--white);font:400 11.5px "Open Sans",sans-serif;padding:2px 0 0 12px}
.login-box{left:470px;top:442px;width:190px;height:82px}
.login-row{display:flex;align-items:center;font-size:7px;color:#222;margin:6px 0 0 12px}
.login-row label{width:58px}
.login-row .field{width:81px;height:12px;border:1px solid #aaa;background:var(--white)}
.login-actions{position:absolute;left:72px;top:62px;display:flex;gap:3px}
.login-actions span{font-size:6.5px;color:#333;background:linear-gradient(#fafafa,#d8d8d8);border:1px solid #aaa;padding:1px 5px}
.solutions-box{left:472px;top:540px;width:189px;height:156px}
.solution-list{list-style:none;margin:6px 0 0 18px;width:119px}
.solution-list li{position:relative;height:19.6px;border-bottom:1px dotted #999;font:400 7.6px "Open Sans",sans-serif;color:#222;padding:7px 0 0 3px}
.solution-list li::after{content:"»";position:absolute;right:2px;top:2px;font-size:9px}
.solution-list li.current{background:#d6d6d6;border-left:3px solid #222;border-bottom:none;padding-left:6px;padding-top:4px;height:18px;margin:1px 0}
.solution-list li.current::after{content:""}

.divider{left:82px;top:718px;width:578px;height:1px;background:#d0d0d0}

.service-card{top:738px;width:134px;height:186px;background:var(--white)}
.service-card h3{height:22px;background:var(--tab-grey);font:400 11.5px "Open Sans",sans-serif;color:#333;text-align:center;padding-top:4px;letter-spacing:.3px}
.service-photo{margin:8px auto 0;width:116px;height:67px}
.service-card p{margin:9px 7px 0;font-size:7.6px;line-height:9.8px;color:#333;text-align:justify}
.service-card .readmore{position:absolute;left:4px;bottom:9px;width:125px;height:18px;background:var(--navy);color:var(--white);font-size:8px;text-align:center;padding-top:4px}

.client-strip{left:72px;top:976px;width:590px;height:48px;z-index:5;background:var(--white);border-radius:12px;box-shadow:0 0 5px rgba(0,0,0,.25);display:flex;align-items:center;justify-content:space-between;padding:0 10px}
.client-badges{display:flex;align-items:center;gap:22px}
.badge{display:block}

.site-footer{left:0;top:1004px;width:734px;height:170px;background:var(--footer)}
.footer-col{top:1050px;color:var(--white)}
.footer-col h4{font:400 13px "Open Sans",sans-serif;margin-bottom:5px}
.footer-col ul{list-style:none;font:400 7.4px "Open Sans",sans-serif;line-height:13.6px}
.footer-sep{top:1056px;width:1px;height:84px;background:#3a3a3a}
.footer-brand{left:513px;top:1072px}
.footer-brand .brand-name{color:var(--white);font-size:9.5px}
.footer-brand .brand-dot{width:26px;height:26px}
.footer-base{left:0;top:1174px;width:734px;height:26px;background:var(--footer-base);font-size:7px;color:#aaa;padding:6px 0 0 94px}
.footer-base span{margin-right:24px}
</style>
</head>
<body>
<div class="canvas">

  <header>
    <div class="abs utility-bar"></div>
    <nav class="abs utility-links">
      <span>Company</span><span>Careers</span><span>Contact</span>
      <span class="call">Call Us : <span>44(0)1632 960418</span></span>
    </nav>
    <svg class="search-icon" width="12" height="12" viewBox="0 0 12 12" aria-hidden="true">
      <circle cx="5" cy="5" r="3.6" fill="none" stroke="#333" stroke-width="1.4"/>
      <line x1="7.6" y1="7.6" x2="11" y2="11" stroke="#333" stroke-width="1.6"/>
    </svg>

    <div class="abs brand site-brand">
      <span class="brand-dot"></span>
      <span class="brand-name">NORTHVALE<br>LOGISTICS</span>
    </div>

    <nav class="abs main-nav">
      <a class="nav-active" href="#">SOLUTIONS</a>
      <a class="nav-processes" href="#">OUR PROCESSES</a>
      <a class="nav-industries" href="#">INDUSTRIES</a>
    </nav>
  </header>

  <div class="abs content-panel"></div>

  <section class="abs hero">
    <div class="abs hero-art" role="img" aria-label="Globe with stacked cardboard shipping boxes"></div>
    <div class="abs hero-title">There Are Many Variations</div>
    <div class="abs hero-sub">New Way To Think</div>
  </section>
  <div class="abs hero-shadow"></div>
  <div class="abs slider-dots"><span class="on"></span><span></span><span></span><span></span></div>

  <main>
    <h1 class="abs welcome-title">Welcome to Northvale Logistics</h1>
    <div class="abs welcome-copy">
      <p>simply dummy text of the printing and typesetting industry. Lorem Ipsum has been the industry's standard dummy text ever since the 1500s, when an unknown printer took a galley of type and scrambled it to make a type specimen book. It has survived not only five centuries,</p>
      <p class="tight">but also the leap into electronic typesetting, remaining essentially unknown printer took a galley of type and scrambled an unknown printer took a galley of type and scrambled unchanged.</p>
      <p>simply dummy text of the printing and typesetting industry. Lorem Ipsum has been the industry's standard dummy text ever since the 1500s, when an unknown printer took a galley of type and scrambled it to make a type specimen book. It has survived not only five centuries,</p>
      <p>but also the leap into electronic typesetting, remaining essentially unknown printer took a galley of type and scrambled an unknown printer took a galley of type and scrambled unchanged.</p>
      <p>but also the leap into electronic typesetting, remaining essentially unknown printer took a galley of type and scrambled an unknown printer took a galley of type and scrambled</p>
    </div>
    <a class="abs read-more">read more &gt;&gt;</a>

    <aside class="abs side-box login-box">
      <div class="side-head">Quick Login</div>
      <div class="login-row"><label>Customer Login:</label><span class="field"></span></div>
      <div class="login-row"><label>Password:</label><span class="field"></span></div>
      <div class="login-actions"><span>Submit</span><span>Reset »</span></div>
    </aside>

    <aside class="abs side-box solutions-box">
      <div class="side-head">Our Solutions</div>
      <ul class="solution-list">
        <li>Omni Channel Distribution</li>
        <li class="current">Reverse Logistics</li>
        <li>Manufacturing Support</li>
        <li>Omni Channel Distribution</li>
        <li>Omni Channel Distribution</li>
        <li>Omni Channel Distribution</li>
      </ul>
    </aside>

    <div class="abs divider"></div>

    <article class="abs service-card" style="left:85px">
      <h3>LOREM IPSUM</h3>
      <div class="service-photo" role="img" aria-label="Row of white freight trucks" style="background:linear-gradient(#cfd6de,#eef0f2 55%,#3a3f46)"></div>
      <p>Lorem Ipsum is simply dummy text of the pring and typesetting industry. Lorem Ipsum has been the industry's standard.</p>
      <span class="readmore">Readmore</span>
    </article>
    <article class="abs service-card" style="left:230px">
      <h3>LOREM IPSUM</h3>
      <div class="service-photo" role="img" aria-label="Passenger jet flying in blue sky" style="background:linear-gradient(#3d6fb4,#a9c6e8 60%,#e6eef7)"></div>
      <p>Lorem Ipsum is simply dummy text of the pring and typesetting industry. Lorem Ipsum has been the industry's standard.</p>
      <span class="readmore">Readmore</span>
    </article>
    <article class="abs service-card" style="left:374px">
      <h3>LOREM IPSUM</h3>
      <div class="service-photo" role="img" aria-label="Warehouse worker beside stacked cartons" style="background:linear-gradient(120deg,#6b5138,#c59a6a 50%,#8a6b4d)"></div>
      <p>Lorem Ipsum is simply dummy text of the pring and typesetting industry. Lorem Ipsum has been the industry's standard.</p>
      <span class="readmore">Readmore</span>
    </article>
    <article class="abs service-card" style="left:518px">
      <h3>LOREM IPSUM</h3>
      <div class="service-photo" role="img" aria-label="Container ship and truck at port" style="background:linear-gradient(#f2f2f2,#b9c0c8 55%,#4b5563)"></div>
      <p>Lorem Ipsum is simply dummy text of the pring and typesetting industry. Lorem Ipsum has been the industry's standard.</p>
      <span class="readmore">Readmore</span>
    </article>
  </main>

  <footer>
    <div class="abs site-footer"></div>
    <div class="abs footer-col" style="left:96px">
      <h4>Quick Links</h4>
      <ul><li>Lorem ipsum dolor sit</li><li>Amet consectetuer</li><li>Adipiscing elit</li><li>Praesent vestibulum</li><li>Molestie lacus aenean</li></ul>
    </div>
    <div class="abs footer-sep" style="left:212px"></div>
    <div class="abs footer-col" style="left:239px">
      <h4>How it Works</h4>
      <ul><li>Lorem ipsum dolor sit</li><li>Amet consectetuer</li><li>Adipiscing elit</li><li>Praesent vestibulum</li><li>Molestie lacus aenean</li></ul>
    </div>
    <div class="abs footer-sep" style="left:356px"></div>
    <div class="abs footer-col" style="left:380px;top:1054px">
      <h4>Contact Us</h4>
      <ul><li>12 Harlow Row</li><li>Kelmont, KM4 2RP</li><li>Phone:+44(0)1632 960418</li><li>Email:hello@northvale.example</li></ul>
    </div>
    <div class="abs brand footer-brand">
      <span class="brand-dot"></span>
      <span class="brand-name">NORTHVALE<br>LOGISTICS</span>
    </div>
    <div class="abs footer-base">
      <span>Home | News | About Us | Solutions | Contact Us</span>
      <span style="margin-right:0">© 2014 Logistics &nbsp;FAQ | Privacy Policy | Site Map.</span>
    </div>
  </footer>

  <div class="abs client-strip">
    <svg width="12" height="18" viewBox="0 0 12 18" aria-hidden="true"><polyline points="10,2 3,9 10,16" fill="none" stroke="#111" stroke-width="2.4"/></svg>
    <div class="client-badges">
      <svg class="badge" width="38" height="22" aria-hidden="true"><rect x="1" y="1" width="36" height="20" fill="none" stroke="#1f6b3a" stroke-width="2"/></svg>
      <svg class="badge" width="28" height="30" aria-hidden="true"><rect x="2" y="4" width="24" height="22" fill="#c4132f"/></svg>
      <svg class="badge" width="28" height="36" aria-hidden="true"><rect x="1" y="1" width="26" height="34" fill="#d46a1a"/></svg>
      <svg class="badge" width="56" height="14" aria-hidden="true"><rect x="0" y="2" width="56" height="10" fill="#222"/></svg>
      <svg class="badge" width="38" height="22" aria-hidden="true"><ellipse cx="19" cy="11" rx="18" ry="10" fill="#1c3a78"/></svg>
      <svg class="badge" width="54" height="30" aria-hidden="true"><circle cx="27" cy="15" r="13" fill="#e2572a"/></svg>
      <svg class="badge" width="44" height="34" aria-hidden="true"><rect x="4" y="3" width="36" height="28" fill="#e0a21a"/></svg>
      <svg class="badge" width="22" height="22" aria-hidden="true"><circle cx="11" cy="11" r="10" fill="#3c9a2e"/></svg>
    </div>
    <svg width="12" height="18" viewBox="0 0 12 18" aria-hidden="true"><polyline points="2,2 9,9 2,16" fill="none" stroke="#111" stroke-width="2.4"/></svg>
  </div>

</div>
</body>
</html>
```